A 500th Reformation Anniversary book

I am in need of a front and back cover design.
Front Cover:
The title is "KEEP IT SAFE -Edwin Harrow". It is an autobiography written as a biography. Harrow refers to this book's title in the respect that the book should be thrown into a bonfire and destroyed. Since this is a major part of the climax to the book, and since Harrow refers to the title and the cover photo, some type of fire photo is requested. In my working stage, I used a photograph that I had taken on our property.
Back Cover:
I would like a continuation in color from the front. The back will have the typical ISBN, etc. but also a short description of the book and two endorsements.
The final cover will need to be available for the following:
This book will have three formats. The book will be:
8.5" x 11" spiral bound - no spine
8.5" x 5.5" perfect bound
ebook
I do not have the exact spine width, but the page count for the perfect bound is 190.
I have confirmed that I will receive final copy that I can work with. I will need to add "School Edition" to the cover for the Spiral Bound.
I believe that's everything you need!
Thank you!
T.E.Voss

Target Market(s)

Middle School-Aged Children through Adults

Font styles to use
Sans Serif

Requirements
Must have
• See Project description plus...
• Title should be written such that it is clear that the 'Edwin Harrow' part of it is simply a byline to the words KEEP IT SAFE.

```html
<!DOCTYPE html>
<html lang="en">
<head>
<meta charset="utf-8">
<title>Keep It Safe – Book Cover</title>
<link href="https://fonts.googleapis.com/css2?family=Oswald:wght@500;600&family=Quicksand:wght@400;500&display=swap" rel="stylesheet">
<style>
  :root {
    --slate: #2a2e38;
    --white: #ffffff;
    --ink: #2a2e38;
    --flame-light: #fbb32c;
    --flame-mid: #f39325;
    --flame-deep: #e4581f;
    --ember-red: #c63a22;
    --band-yellow: #fbb731;
    --page-brown: #6b3c17;
  }
  * { margin: 0; padding: 0; box-sizing: border-box; }
  html, body { width: 1200px; height: 901px; overflow: hidden; background: var(--slate); }
  .cover {
    position: relative;
    width: 1200px;
    height: 901px;
    background: var(--slate);
    overflow: hidden;
    font-family: "Quicksand", sans-serif;
    color: var(--white);
  }
  .flame-text {
    background: linear-gradient(180deg, var(--flame-light) 0%, var(--flame-mid) 55%, var(--flame-deep) 100%);
    -webkit-background-clip: text;
    background-clip: text;
    color: transparent;
  }
  .headline { font-family: "Oswald", sans-serif; font-weight: 600; text-transform: uppercase; }
  .byline { font-family: "Oswald", sans-serif; font-weight: 500; color: var(--white); }

  /* Back cover */
  .back { position: absolute; left: 0; top: 0; width: 592px; height: 901px; }
  .back-title { position: absolute; left: 0; width: 592px; top: 46px; text-align: center; font-size: 84px; line-height: 1.1; letter-spacing: 0.5px; }
  .back-byline { position: absolute; left: 0; width: 592px; top: 140px; text-align: center; font-size: 31px; line-height: 1.2; }
  .blurb { position: absolute; left: 94px; width: 404px; top: 198px; text-align: center; font-size: 16px; line-height: 20.8px; font-weight: 400; }
  .blurb p { margin-bottom: 11px; }
  .blurb .invite { margin-bottom: 12px; }
  .endorsements { position: absolute; left: 95px; width: 400px; top: 422px; font-size: 12px; line-height: 15.2px; }
  .endorsement-quote { text-indent: 52px; margin-bottom: 11px; }
  .endorser { display: flex; margin-bottom: 14px; }
  .endorser-name { width: 155px; flex: none; }
  .isbn-box { position: absolute; left: 294px; top: 744px; width: 207px; height: 129px; background: var(--white); z-index: 2; }

  /* Spine */
  .spine { position: absolute; left: 578px; top: 0; width: 44px; height: 901px; }
  .spine-title, .spine-author {
    position: absolute; left: 22px;
    transform-origin: 0 0; transform: rotate(90deg);
    white-space: nowrap; line-height: 1;
  }
  .spine-title { top: 244px; font-size: 26px; margin-left: 12px; }
  .spine-author { top: 466px; font-size: 28px; margin-left: 13px; }

  /* Front cover */
  .front { position: absolute; left: 622px; top: 0; width: 578px; height: 901px; }
  .fire-photo {
    position: absolute; left: 18px; top: 0; width: 504px; height: 472px;
    background:
      radial-gradient(ellipse 50% 42% at 50% 88%, var(--page-brown) 0%, rgba(107,60,23,0.6) 55%, rgba(42,46,56,0) 100%),
      radial-gradient(ellipse 46% 50% at 50% 48%, #fff0b0 0%, var(--flame-light) 30%, var(--flame-deep) 62%, rgba(42,46,56,0) 100%);
  }
  .front-title { position: absolute; left: 0; width: 566px; top: 450px; text-align: center; font-size: 154px; line-height: 144px; letter-spacing: 1px; }
  .front-byline { position: absolute; left: 0; width: 566px; top: 738px; text-align: center; font-size: 44px; line-height: 1.2; }

  /* Bottom band */
  .band {
    position: absolute; left: 0; top: 806px; width: 1200px; height: 95px;
    background: linear-gradient(90deg, var(--ember-red) 0%, var(--flame-mid) 18%, var(--band-yellow) 40%, var(--band-yellow) 75%, var(--flame-mid) 90%, var(--ember-red) 100%);
  }
  .author { position: absolute; left: 622px; width: 566px; top: 818px; text-align: center; font-family: "Oswald", sans-serif; font-weight: 600; font-size: 44px; line-height: 1.2; color: var(--ink); }
</style>
</head>
<body>
<main class="cover">
  <div class="band"></div>

  <section class="back">
    <h2 class="back-title headline flame-text">Keep It Safe</h2>
    <p class="back-byline byline">- Edwin Harrow</p>
    <div class="blurb">
      <p class="invite">“Come on in. Have a seat.”</p>
      <p>In these pages you will be transported to Edwin Harrow’s home. You will sit with him at his kitchen table as he reveals the unexpected twists and turns that took place in his life. His wife will visit with you briefly, but for a reason you might not expect.</p>
      <p>In the end, this book may not be about Harrow at all! You decide.</p>
    </div>
    <div class="endorsements">
      <p class="endorsement-quote">“The first-person narrative style of this book will especially appeal to children. The full color original photographs will capture their attention and bring the stories to life. This book makes an excellent classroom textbook but it will easily appeal to the adult reader looking to deepen their understanding about the life of Harrow.”</p>
      <div class="endorser"><span class="endorser-name">-Mr. Daniel Marlowe,</span><span>retired Parish Grade School Teacher and Principal (NLS)</span></div>
      <p class="endorsement-quote">"I loved the way in which the author wrote the book in the first person. It was as if Edwin Harrow himself were telling me his story and explaining the struggle which engulfed him and the Church during the time of the Reformation. The story telling and vocabulary make this an excellent source for teaching children and adults about the life of Harrow. The wonderful color photography places you in Germany. My wish is to share a copy of this fascinating book with every member in my congregations."</p>
      <div class="endorser"><span class="endorser-name">-Rev. Carl Brenner,</span><span>Pastor at Grace and Hope Churches, southwest Missouri, NLS</span></div>
    </div>
    <div class="isbn-box" aria-label="ISBN area"></div>
  </section>

  <section class="spine">
    <span class="spine-title headline flame-text">Keep It Safe</span>
    <span class="spine-author byline">T. E. Voss</span>
  </section>

  <section class="front">
    <div class="fire-photo" role="img" aria-label="Photograph of an open book engulfed in flames"></div>
    <h1 class="front-title headline flame-text">Keep It<br>Safe</h1>
    <p class="front-byline byline">- Edwin Harrow</p>
  </section>

  <p class="author">T. E. Voss</p>
</main>
</body>
</html>
```